Modern business card for triathlon training business in Australia

We need a business card design for our triathlon training company.

Lakeshore Pace Fitness is an Australian business, owned by women, run for women. Lakeshore Pace Fitness helps women prepare or improve triathlon skills and confidence through triathlon camps completely designed for women.

Our camps focus on preparing women both physically and mentally for their next (or first!) triathlon.

You can see our website www.lakeshorepacefitness.com.au for more info about our business and our style.

We've attached two of our logos and are happy to consider a design that utilised either colour scheme with the teal colour being our 'feature' colour. We don't want overly feminine cards but rather cards that are professional and neat. If the inclusion of any pictures/art is warranted, this should be focused on our swim/ride/run theme and in that specific order (swim/ride/run).

The business card needs to be a printable design and the contact details will need to change for our two employees.

Target Market(s)

Female clients and partners/vendors/sponsors that we work with in the triathlon industry

Industry/Entity Type

Fitness

Contact Information for Business Card

Lakeshore Pace Fitness (business name)
Maren Dunley
Business Director
Mobile: 0455 918 237
Email: maren@lakeshorepacefitness.com.au
www.lakeshorepacefitness.com.au

Second business card:
Lakeshore Pace Fitness
Bea Calvert
Coaching Director
Mobile: 0433 206 519
Email: bea@lakeshorepacefitness.com.au

Font styles to use
Serif
Sans Serif

Requirements
Must have
• Core contact details above, our logo and be a printable design
Should not have
• Pink
• Cursive/script fonts

```html
<!DOCTYPE html>
<html lang="en">
<head>
<meta charset="utf-8">
<title>Lakeshore Pace Fitness – Business Card</title>
<link href="https://fonts.googleapis.com/css2?family=Questrial&family=Oswald:wght@600&family=Tinos&display=swap" rel="stylesheet">
<style>
  :root {
    --page-bg: #e9e7e3;
    --card-white: #fbfbfa;
    --teal: #2fc3cf;
    --band-grey: #a9aaac;
    --band-light: #cfd0d2;
    --ink: #1e1e1e;
    --logo-teal: #45c6d0;
  }
  html, body {
    margin: 0;
    padding: 0;
    width: 1200px;
    height: 1000px;
    overflow: hidden;
    background: var(--page-bg);
  }
  .stage {
    position: relative;
    width: 1200px;
    height: 1000px;
  }
  .card {
    position: absolute;
    left: 150px;
    top: 225px;
    width: 900px;
    height: 550px;
    background: var(--card-white);
    box-shadow: 0 10px 30px rgba(0,0,0,0.15);
    overflow: hidden;
  }
  .brand {
    position: absolute;
    left: 50px;
    top: 195px;
    width: 300px;
    display: flex;
    align-items: center;
    gap: 14px;
    font-family: "Questrial", sans-serif;
    font-size: 28px;
    line-height: 1.15;
    letter-spacing: 1px;
    color: var(--logo-teal);
    text-transform: uppercase;
  }
  .brand-dot {
    flex: 0 0 auto;
    width: 26px;
    height: 26px;
    border-radius: 50%;
    background: var(--logo-teal);
  }
  .brand-name {
    display: block;
    width: 240px;
  }
  .person {
    position: absolute;
    left: 400px;
    top: 195px;
  }
  .person-name {
    font-family: "Questrial", sans-serif;
    font-size: 40px;
    color: var(--ink);
    line-height: 1;
    letter-spacing: 0.5px;
  }
  .person-role {
    font-family: "Oswald", sans-serif;
    font-weight: 600;
    font-size: 20px;
    color: var(--teal);
    line-height: 1.2;
    margin-top: 6px;
  }
  .contact {
    position: absolute;
    right: 40px;
    top: 300px;
    text-align: right;
    font-family: "Tinos", serif;
    font-size: 17px;
    line-height: 1.2;
    color: var(--ink);
  }
  .contact-phone { margin-bottom: 38px; }
  .band {
    position: absolute;
    left: 0;
    right: 0;
    bottom: 30px;
    height: 78px;
  }
  .band-top {
    position: absolute;
    left: 0; right: 0; top: 0;
    height: 14px;
    background: var(--band-light);
  }
  .band-accent {
    position: absolute;
    left: 0; right: 0; top: 14px;
    height: 8px;
    background: var(--teal);
  }
  .band-gap {
    position: absolute;
    left: 0; right: 0; top: 22px;
    height: 6px;
    background: var(--card-white);
  }
  .band-main {
    position: absolute;
    left: 0; right: 0; top: 28px;
    height: 50px;
    background: var(--band-grey);
  }
</style>
</head>
<body>
  <main class="stage">
    <section class="card" aria-label="Business card front">
      <div class="brand">
        <span class="brand-dot"></span>
        <span class="brand-name">Lakeshore Pace Fitness</span>
      </div>

      <div class="person">
        <div class="person-name">Maren Dunley</div>
        <div class="person-role">Business Director</div>
      </div>

      <div class="contact">
        <div class="contact-phone">0455 918 237</div>
        <div class="contact-web">www.lakeshorepacefitness.com.au</div>
        <div class="contact-email">maren@lakeshorepacefitness.com.au</div>
      </div>

      <div class="band">
        <div class="band-top"></div>
        <div class="band-accent"></div>
        <div class="band-gap"></div>
        <div class="band-main"></div>
      </div>
    </section>
  </main>
</body>
</html>
```